Stationery Design Project

I am a personal trainer in the fitness industry based in Miami. I have recently designed a logo for my company, now i need to market my name through selected stationery designs.
I need an email signature, invoice and a business card. I am looking for a design that is fresh and eye catching to my target audience.
Updates

Reason: Waiting for photo to be taken for business card.

Target Market(s)

25 to 65 years old - male and female - overweight, sedentary and athletic clientele - middle to wealthy economic class

Industry/Entity Type

Personal Trainer

Requirements
Must have
• Will attach Zip file with logo, template of invoice and personal information.
Will attach photo for business card in the next few days.
Nice to have
• Black backdrop logo image for banner of Invoice, with transparent images of my logo.
White backdrop logo image for Email signature, with font that works well with logo.

```html
<!DOCTYPE html>
<html lang="en">
<head>
<meta charset="utf-8">
<title>Invoice – Corestride Training</title>
<link href="https://fonts.googleapis.com/css2?family=Source+Sans+3:wght@400;600;700&display=swap" rel="stylesheet">
<style>
  :root {
    --paper: #ffffff;
    --ink: #3a3a3c;
    --ink-soft: #555559;
    --accent: #e2702a;
    --panel: #c7c7cc;
    --rule: #e4e4e7;
    --ink-strong: #111111;
  }
  * { margin: 0; padding: 0; box-sizing: border-box; }
  html, body { width: 932px; height: 1200px; overflow: hidden; background: var(--paper); }
  body { font-family: "Source Sans 3", Arial, sans-serif; color: var(--ink); position: relative; }

  .sender { position: absolute; left: 44px; top: 98px; font-size: 16px; line-height: 21.5px; color: var(--ink-soft); }
  .sender sup { font-size: 10px; }

  .brand { position: absolute; left: 331px; top: 100px; width: 300px; text-align: center; }
  .brand-dot { display: block; width: 84px; height: 84px; margin: 0 auto 18px; border-radius: 50%; background: var(--accent); }
  .brand-name { font-size: 30px; font-weight: 700; color: var(--accent); letter-spacing: 1px; line-height: 1; text-transform: uppercase; }

  .doc-title { position: absolute; right: 50px; top: 98px; font-size: 40px; font-weight: 700; color: var(--accent); letter-spacing: 0.5px; }

  .contact { position: absolute; left: 44px; top: 258px; font-size: 16px; line-height: 27px; color: var(--ink-soft); }

  .doc-meta { position: absolute; left: 775px; top: 258px; font-size: 12px; line-height: 24px; color: var(--ink-soft); text-transform: uppercase; }

  .bill-to { position: absolute; left: 160px; top: 380px; width: 612px; height: 132px; background: var(--panel); }
  .bill-to .row { height: 22px; border-bottom: 1px solid var(--rule); }
  .bill-to .row:first-child { height: 22px; margin-top: 14px; }
  .bill-label { position: absolute; left: 28px; top: 20px; font-size: 17px; font-weight: 700; color: var(--ink-strong); }
  .bill-lines { position: absolute; left: 146px; top: 22px; font-size: 12.5px; line-height: 22px; color: var(--ink-strong); }

  .items { position: absolute; left: 34px; top: 550px; width: 868px; border-collapse: collapse; background: var(--panel); font-size: 13px; color: var(--ink-strong); }
  .items th, .items td { border: 1px solid var(--rule); }
  .items th { height: 30px; font-weight: 400; font-size: 12px; text-transform: uppercase; }
  .items td { height: 28px; }
  .items .first td { height: 44px; vertical-align: middle; }
  .col-qty { width: 111px; text-align: center; }
  .col-desc { width: 478px; text-align: left; padding-left: 15px; }
  .col-unit { width: 152px; text-align: right; padding-right: 12px; }
  .col-total { width: 127px; text-align: right; padding-right: 20px; }
  .items th.col-desc { text-align: center; padding-left: 0; }
  .items th.col-unit, .items th.col-total { text-align: center; padding-right: 0; }
  .items td.col-qty { line-height: 16px; }

  .totals { position: absolute; left: 623px; top: 939px; width: 279px; border-collapse: collapse; background: var(--panel); font-size: 12.5px; color: var(--ink-strong); }
  .totals td { height: 26px; border-bottom: 1px solid var(--rule); }
  .totals .label { width: 152px; text-align: right; padding-right: 14px; font-weight: 700; text-transform: uppercase; }
  .totals .value { text-align: right; padding-right: 20px; }

  .payable { position: absolute; left: 36px; top: 1026px; font-size: 19px; color: var(--ink-strong); }

  .thanks { position: absolute; left: 0; width: 932px; top: 1085px; text-align: center; font-size: 19px; font-weight: 700; letter-spacing: 2.5px; color: var(--ink-strong); text-transform: uppercase; }
</style>
</head>
<body>
  <address class="sender" style="font-style:normal">
    Dana Reyes<br>
    88 North West 9<sup>th</sup> Street<br>
    Apartment 1204<br>
    Miami, FL 33128<br>
    Mobile 305 - 555 - 0142
  </address>

  <div class="brand">
    <span class="brand-dot"></span>
    <div class="brand-name">Corestride Training</div>
  </div>

  <h1 class="doc-title">INVOICE</h1>

  <div class="contact">
    dana@corestridetraining.com<br>
    Training Location: The Bayfront
  </div>

  <div class="doc-meta">
    Invoice # 0000<br>
    Date: 00/00/2012
  </div>

  <section class="bill-to">
    <div class="row"></div><div class="row"></div><div class="row"></div><div class="row"></div><div class="row"></div>
    <div class="bill-label">BILL TO:</div>
    <div class="bill-lines">XXXXXXXXXXX<br>XXXXXXXXXXX<br>XXXXX, FL<br>XXXXX</div>
  </section>

  <table class="items">
    <thead>
      <tr><th class="col-qty">Qty</th><th class="col-desc">Description</th><th class="col-unit">Unit Price</th><th class="col-total">Line Total</th></tr>
    </thead>
    <tbody>
      <tr class="first"><td class="col-qty">Session<br>Package</td><td class="col-desc">Personal Training</td><td class="col-unit">$00</td><td class="col-total">$000</td></tr>
      <tr><td class="col-qty"></td><td class="col-desc"></td><td class="col-unit"></td><td class="col-total"></td></tr>
      <tr><td class="col-qty"></td><td class="col-desc"></td><td class="col-unit"></td><td class="col-total"></td></tr>
      <tr><td class="col-qty"></td><td class="col-desc"></td><td class="col-unit"></td><td class="col-total"></td></tr>
      <tr><td class="col-qty"></td><td class="col-desc"></td><td class="col-unit"></td><td class="col-total"></td></tr>
      <tr><td class="col-qty"></td><td class="col-desc"></td><td class="col-unit"></td><td class="col-total"></td></tr>
      <tr><td class="col-qty"></td><td class="col-desc"></td><td class="col-unit"></td><td class="col-total"></td></tr>
      <tr><td class="col-qty"></td><td class="col-desc"></td><td class="col-unit"></td><td class="col-total"></td></tr>
      <tr><td class="col-qty"></td><td class="col-desc"></td><td class="col-unit"></td><td class="col-total"></td></tr>
      <tr><td class="col-qty"></td><td class="col-desc"></td><td class="col-unit"></td><td class="col-total"></td></tr>
      <tr><td class="col-qty"></td><td class="col-desc"></td><td class="col-unit"></td><td class="col-total"></td></tr>
    </tbody>
  </table>

  <table class="totals">
    <tr><td class="label">Subtotal</td><td class="value">$000.00</td></tr>
    <tr><td class="label">Sales Tax</td><td class="value">-</td></tr>
    <tr><td class="label">Total</td><td class="value">$000.00</td></tr>
  </table>

  <p class="payable">Please make all checks payable to Dana Reyes.</p>

  <p class="thanks">Thank you for your business</p>
</body>
</html>
```